Lumen Ridge Agency Stationery
Lumen Ridge
Project: Lumen Ridge Agency Stationery
Lumen Ridge Agency Stationery - Advertising
Creative Brief
Simple
Doris Jean Malloway
Vice President, Corporate Operations
482 Fenwick Ave. Seattle, WA 98112
info@lumenridgeco.example
dorisjean@lumenridgeco.example
www.lumenridgeco.example
Front should have black background with LR circle only (no text). Would love to see the red circle and red plus raised to give them a 3-D look. You can do a standard rectangle business card or change it up and make it a circle.
Back should also be black background with white font. Occasionally you can use a red font if it looks cool to distinguish individual fields. Around the border of the card should be the company information (Address field, phone number (toll-free field), email (fax field), and website. Inside the center should be the person's name, title, direct line (phone field) and email. You can put the logo in the center again if it looks like to have that on the left and contact info on right, but it is not necessary to use the logo again. You can also try using icons with the text fields, but if it looks too busy, then don't worry about it. Thanks!

```html
<!DOCTYPE html>
<html lang="en">
<head>
<meta charset="utf-8">
<title>Lumen Ridge Agency Stationery</title>
<link rel="stylesheet" href="https://fonts.googleapis.com/css2?family=Open+Sans:wght@400;600&display=swap">
<style>
  :root {
    --stage: #e4e4e4;
    --card-black: #0d0d0d;
    --brand-red: #e3161b;
    --white: #ffffff;
    --faint: #262626;
  }
  * { margin: 0; padding: 0; box-sizing: border-box; }
  html, body {
    width: 1200px; height: 984px; overflow: hidden;
    background: var(--stage);
    font-family: "Open Sans", Arial, sans-serif;
  }
  .card {
    position: absolute;
    width: 640px; height: 366px;
    border-radius: 22px;
    background: var(--card-black);
    overflow: hidden;
    box-shadow: 0 14px 30px rgba(0,0,0,0.25);
  }
  .card--front { left: 400px; top: 70px; }
  .card--back { left: 180px; top: 520px; }

  /* Front: faint company name and website */
  .company-faint {
    position: absolute; left: 0; right: 0; top: 100px;
    text-align: center;
    font-size: 96px; font-weight: 400; line-height: 1;
    color: var(--faint);
  }
  .website-large {
    position: absolute; left: 0; right: 0; top: 300px;
    text-align: center;
    font-size: 22px; letter-spacing: 4px; color: var(--white);
  }
  .website-large .accent { color: var(--brand-red); }

  /* Back: identity side */
  .swoosh { position: absolute; inset: 0; }
  .brand { position: absolute; left: 44px; top: 30px; }
  .brand-circle {
    width: 96px; height: 96px; border-radius: 50%;
    background: var(--brand-red);
    border: 4px solid var(--white);
  }
  .brand-name {
    margin-top: 6px;
    font-size: 24px; font-weight: 400; line-height: 32px; color: var(--white);
  }
  .person-name {
    position: absolute; left: 44px; top: 172px;
    font-size: 15px; font-weight: 600; line-height: 20px; color: var(--brand-red);
  }
  .person-title {
    position: absolute; left: 44px; top: 194px;
    font-size: 11px; line-height: 15px; color: var(--white);
  }
  .contact-list {
    position: absolute; left: 392px; top: 228px;
    list-style: none;
  }
  .contact-list li {
    display: flex; align-items: center; gap: 7px;
    height: 19px;
    font-size: 10px; color: var(--white);
  }
  .contact-list svg { width: 12px; height: 12px; flex: none; }
</style>
</head>
<body>

<section class="card card--front" aria-label="Business card front">
  <div class="company-faint">Lumen Ridge</div>
  <div class="website-large">www.<span class="accent">lumenridgeco</span>.example</div>
</section>

<section class="card card--back" aria-label="Business card back">
  <svg class="swoosh" viewBox="0 0 640 366" preserveAspectRatio="none" aria-hidden="true">
    <path d="M0 250 C 160 300, 380 160, 640 150 L640 366 L0 366 Z" fill="#ffffff"/>
    <path d="M0 260 C 160 310, 380 170, 640 160 L640 366 L0 366 Z" fill="#0d0d0d"/>
    <path d="M0 272 C 160 322, 380 182, 640 172 L640 366 L0 366 Z" fill="#e3161b"/>
  </svg>

  <div class="brand">
    <div class="brand-circle"></div>
    <div class="brand-name">Lumen Ridge</div>
  </div>
  <div class="person-name">Doris Jean Malloway</div>
  <div class="person-title">Vice President, Corporate Operations</div>

  <ul class="contact-list">
    <li>
      <svg viewBox="0 0 12 12"><circle cx="6" cy="6" r="6" fill="#fff"/><path d="M6 2.5a2 2 0 0 0-2 2c0 1.5 2 4.5 2 4.5s2-3 2-4.5a2 2 0 0 0-2-2z" fill="#e3161b"/></svg>
      482 Fenwick Ave. Seattle, WA 98112
    </li>
    <li>
      <svg viewBox="0 0 12 12"><circle cx="6" cy="6" r="6" fill="#fff"/><path d="M4 3l1.2 1.6-.7.8a4 4 0 0 0 2.1 2.1l.8-.7L9 8l-.6.9C6 9 3 6 3.1 3.6z" fill="#e3161b"/></svg>
      206.555.0142
    </li>
    <li>
      <svg viewBox="0 0 12 12"><circle cx="6" cy="6" r="6" fill="#fff"/><path d="M4 3l1.2 1.6-.7.8a4 4 0 0 0 2.1 2.1l.8-.7L9 8l-.6.9C6 9 3 6 3.1 3.6z" fill="#e3161b"/></svg>
      206.555.0187
    </li>
    <li>
      <svg viewBox="0 0 12 12"><circle cx="6" cy="6" r="6" fill="#fff"/><rect x="3" y="4" width="6" height="4" fill="#e3161b"/><path d="M3 4l3 2.2L9 4" stroke="#fff" stroke-width="0.6" fill="none"/></svg>
      info@lumenridgeco.example
    </li>
    <li>
      <svg viewBox="0 0 12 12"><circle cx="6" cy="6" r="6" fill="#fff"/><rect x="3" y="4" width="6" height="4" fill="#e3161b"/><path d="M3 4l3 2.2L9 4" stroke="#fff" stroke-width="0.6" fill="none"/></svg>
      dorisjean@lumenridgeco.example
    </li>
    <li>
      <svg viewBox="0 0 12 12"><circle cx="6" cy="6" r="6" fill="#fff"/><circle cx="6" cy="6" r="3" fill="none" stroke="#e3161b" stroke-width="0.9"/><path d="M3 6h6M6 3v6" stroke="#e3161b" stroke-width="0.7"/></svg>
      www.lumenridgeco.example
    </li>
  </ul>
</section>

</body>
</html>
```